Innovative modern square business card design for law firm

We require a highly modern innovative styled SQUARE business card (double sided) design & layout for our law firm (PLUS an accompanying letterhead design), which specialises mainly in criminal defence. However included somewhere in the design should display the icons representative of all four different areas of law in which the firm offers services. Each card to display the name of the lawyer, job title, telephone number, switchboard, email, web address, facebook & twitter details + physical address. Attached is the main logo + icons of each of the other departments to be included as well as the firms main overhaul icon (all of which can be used or blended into the overall in some way.(note. high res versions of these icons can be provided if required by the design))

Law Firm

```html
<!DOCTYPE html>
<html lang="en">
<head>
<meta charset="utf-8">
<title>Halbrook Defence – Square Business Card</title>
<link href="https://fonts.googleapis.com/css2?family=Arimo:wght@400;700&family=Cinzel:wght@600&display=swap" rel="stylesheet">
<style>
  :root {
    --stage: #e9ebee;
    --navy-deep: #0a2c47;
    --navy: #134568;
    --ink: #1d3c5a;
    --grey: #555b62;
    --dark: #2b2f33;
    --paper: #fbfbfb;
    --white: #ffffff;
    --dept-red: #c8202f;
    --dept-gold: #e8a51c;
    --dept-green: #1f3d25;
    --dept-blue: #1f35a8;
  }
  * { box-sizing: border-box; margin: 0; padding: 0; }
  html, body { width: 1200px; height: 1000px; overflow: hidden; }
  body {
    background: var(--stage);
    font-family: "Arimo", Arial, sans-serif;
    position: relative;
  }
  .card {
    position: absolute;
    top: 240px;
    width: 520px;
    height: 520px;
    box-shadow: 0 6px 18px rgba(0,0,0,.18);
    overflow: hidden;
  }

  /* Back side */
  .card-back {
    left: 50px;
    background: radial-gradient(circle at 60% 30%, var(--navy) 0%, var(--navy-deep) 75%);
    color: var(--white);
  }
  .dept-row {
    position: absolute;
    top: 64px;
    left: 0;
    width: 100%;
    display: flex;
    justify-content: center;
    gap: 36px;
  }
  .dept { width: 40px; height: 36px; border-radius: 4px; }
  .dept-red { background: var(--dept-red); }
  .dept-gold { background: var(--dept-gold); }
  .dept-green { background: var(--dept-green); }
  .dept-blue { background: var(--dept-blue); }
  .back-brand {
    position: absolute;
    top: 180px;
    left: 64px;
    display: flex;
    align-items: center;
    gap: 22px;
  }
  .back-mark { width: 100px; height: 116px; background: var(--white); border-radius: 6px; flex: none; }
  .back-name {
    font-family: "Cinzel", serif;
    font-weight: 600;
    font-size: 42px;
    line-height: 1.05;
    letter-spacing: 1px;
  }
  .back-phone {
    position: absolute;
    top: 330px;
    left: 64px;
    font-size: 16px;
    letter-spacing: 2px;
  }

  /* Front side */
  .card-front {
    left: 630px;
    background: var(--paper);
    color: var(--grey);
  }
  .front-brand {
    position: absolute;
    top: 40px;
    left: 36px;
  }
  .front-brand-row { display: flex; align-items: center; gap: 12px; }
  .front-mark { width: 48px; height: 48px; background: var(--ink); border-radius: 3px; flex: none; }
  .front-name {
    font-family: "Cinzel", serif;
    font-weight: 600;
    font-size: 24px;
    line-height: 1.05;
    color: var(--ink);
  }
  .front-phone { margin-top: 8px; font-size: 10px; color: var(--ink); letter-spacing: .5px; }

  .person {
    position: absolute;
    top: 140px;
    left: 260px;
  }
  .person-name {
    font-size: 23px;
    font-weight: 700;
    letter-spacing: 1.5px;
    color: var(--ink);
    white-space: nowrap;
  }
  .person-name span { color: var(--dark); }
  .person-role {
    font-size: 17px;
    letter-spacing: 8px;
    color: var(--grey);
    margin-top: 4px;
  }

  .social {
    position: absolute;
    top: 232px;
    left: 36px;
    list-style: none;
  }
  .social li {
    display: flex;
    align-items: center;
    gap: 12px;
    font-size: 18px;
    letter-spacing: 2px;
    margin-bottom: 12px;
  }
  .social-dot {
    width: 26px; height: 26px;
    border: 1.5px solid var(--ink);
    border-radius: 50%;
    flex: none;
  }
  .web {
    position: absolute;
    top: 340px;
    left: 36px;
    font-size: 18px;
    letter-spacing: 2px;
  }
  .web strong { color: var(--ink); font-weight: 700; }

  .contact {
    position: absolute;
    top: 232px;
    left: 260px;
    width: 230px;
    height: 190px;
    border-left: 1px solid var(--ink);
    padding-left: 16px;
  }
  .contact-line {
    display: flex;
    align-items: center;
    gap: 12px;
    font-size: 16px;
    letter-spacing: 1.5px;
    margin-bottom: 10px;
    white-space: nowrap;
  }
  .contact-line svg { width: 14px; height: 14px; fill: var(--ink); flex: none; }
  .address { margin-top: 22px; font-size: 16px; letter-spacing: 1.5px; line-height: 1.2; }
  .address-label { color: var(--ink); font-weight: 700; display: block; }
</style>
</head>
<body>

<section class="card card-back" aria-label="Card back">
  <div class="dept-row" aria-label="Practice areas">
    <div class="dept dept-red"></div>
    <div class="dept dept-gold"></div>
    <div class="dept dept-green"></div>
    <div class="dept dept-blue"></div>
  </div>
  <div class="back-brand">
    <div class="back-mark"></div>
    <div class="back-name">Halbrook<br>Defence</div>
  </div>
  <div class="back-phone">0800 555 010 (24hrs)</div>
</section>

<section class="card card-front" aria-label="Card front">
  <div class="front-brand">
    <div class="front-brand-row">
      <div class="front-mark"></div>
      <div class="front-name">Halbrook<br>Defence</div>
    </div>
    <div class="front-phone">0800 555 010 (24hrs)</div>
  </div>

  <div class="person">
    <div class="person-name">Daniel <span>Whitford</span></div>
    <div class="person-role">Designer</div>
  </div>

  <ul class="social">
    <li><span class="social-dot"></span>username</li>
    <li><span class="social-dot"></span>username</li>
  </ul>
  <div class="web">www.<strong>website</strong>.com</div>

  <div class="contact">
    <div class="contact-line">
      <svg viewBox="0 0 24 24" aria-hidden="true"><path d="M6.6 10.8a15 15 0 0 0 6.6 6.6l2.2-2.2a1 1 0 0 1 1-.25 11.4 11.4 0 0 0 3.6.57 1 1 0 0 1 1 1V20a1 1 0 0 1-1 1A17 17 0 0 1 3 4a1 1 0 0 1 1-1h3.5a1 1 0 0 1 1 1c0 1.25.2 2.45.57 3.57a1 1 0 0 1-.25 1z"/></svg>
      123.456.789
    </div>
    <div class="contact-line">
      <svg viewBox="0 0 24 24" aria-hidden="true"><path d="M2 5h20v14H2z"/><path d="M2 5l10 8 10-8" fill="none" stroke="#fbfbfb" stroke-width="2"/></svg>
      Name@website.com
    </div>
    <div class="address">
      <span class="address-label">Address</span>
      123 AN ST., location,<br>country
    </div>
  </div>
</section>

</body>
</html>
```